Price Trend Graphic for Estimates

I want to add a graphic to my estimates that shows the projected price trend of the work we are quoting to the customer. I have attached a couple ideas I was working on but they are garbage. Hopefully you can see the intent and make it look a lot better. Basically I want the customer to see a really a professional / technological graphic that will stimulate them to purchase Right Now! before the price goes up further. So maybe if the "Today's Price" looks nice and friendly and then becomes more critical and ominous as it goes forward 30 days.... 90 days.... Idea is to psychologically

Target Market(s)

Customers for our Construction business

Industry/Entity Type

Construction

Colors
0054AA
0677BA
7BADD7
CADEEF
E8F1F8
0094D4
00A9DD
6FCCEA
C7EBF8
E9F6FB
FFF300
FFF600
FEFA6F
FFFEC7
FFFEE8
F0912C
F2A743
F7CA91
FBE8D2
FDF5EE

Requirements
Must have
• nice looking graphic with upwards moving arrow and 3 price points
Nice to have
• technological / modern looking chart

```html
<!DOCTYPE html>
<html lang="en">
<head>
<meta charset="utf-8">
<title>Price Trend Graphic</title>
<link rel="stylesheet" href="https://fonts.googleapis.com/css2?family=Poppins:wght@300;400;600;700&display=swap">
<style>
  :root {
    --ink-dark: #080a18;
    --panel: #1f1f1f;
    --stage-light: #2b2b2b;
    --stage-dark: #050505;
    --white: #ffffff;
    --muted: #cfcfcf;
    --teal-a: #12b0a6;
    --teal-b: #36d09a;
    --gold-a: #c7902a;
    --gold-b: #b89a55;
    --red-a: #8e1a2a;
    --red-b: #9a3232;
    --pink: #e5466a;
  }
  html, body {
    margin: 0;
    padding: 0;
    width: 846px;
    height: 1200px;
    overflow: hidden;
    background: var(--ink-dark);
  }
  .artboard {
    display: block;
    width: 846px;
    height: 1200px;
    font-family: "Poppins", sans-serif;
  }
  .axis-label { fill: var(--white); font-size: 13px; font-weight: 400; }
  .trend-label { fill: var(--white); font-size: 13px; font-weight: 400; }
  .trend-label--bold { font-weight: 700; }
  .tagline { fill: var(--white); font-size: 20px; font-weight: 300; }
  .tagline--bold { font-weight: 700; }
  .point-title { fill: var(--white); font-weight: 700; }
  .point-sub { fill: var(--white); font-weight: 400; }
  .point-sub--muted { fill: var(--muted); }
  .price { fill: var(--white); font-weight: 700; }
  .price--faded { fill: #d8d8d8; }
</style>
</head>
<body>
<svg class="artboard" viewBox="0 0 780 1106" xmlns="http://www.w3.org/2000/svg" text-anchor="middle">
  <defs>
    <linearGradient id="stage-bg" x1="0" y1="0" x2="1" y2="0.3">
      <stop offset="0" stop-color="var(--stage-light)"/>
      <stop offset="1" stop-color="var(--stage-dark)"/>
    </linearGradient>
    <linearGradient id="teal-fill" x1="0" y1="0" x2="1" y2="1">
      <stop offset="0" stop-color="var(--teal-a)"/>
      <stop offset="1" stop-color="var(--teal-b)"/>
    </linearGradient>
    <linearGradient id="gold-fill" x1="0" y1="0" x2="1" y2="1">
      <stop offset="0" stop-color="var(--gold-a)"/>
      <stop offset="1" stop-color="var(--gold-b)"/>
    </linearGradient>
    <linearGradient id="red-fill" x1="0" y1="0" x2="1" y2="1">
      <stop offset="0" stop-color="#a31d2c"/>
      <stop offset="1" stop-color="var(--red-b)"/>
    </linearGradient>
    <linearGradient id="bar-teal" x1="0" y1="0" x2="0" y2="1">
      <stop offset="0" stop-color="#1c6a63" stop-opacity="0.55"/>
      <stop offset="1" stop-color="#1a4a47" stop-opacity="0.5"/>
    </linearGradient>
    <linearGradient id="bar-gold" x1="0" y1="0" x2="0" y2="1">
      <stop offset="0" stop-color="#5a4622" stop-opacity="0.6"/>
      <stop offset="1" stop-color="#3e3520" stop-opacity="0.55"/>
    </linearGradient>
    <linearGradient id="bar-red" x1="0" y1="0" x2="0" y2="1">
      <stop offset="0" stop-color="#5a1e26" stop-opacity="0.6"/>
      <stop offset="1" stop-color="#3d2226" stop-opacity="0.55"/>
    </linearGradient>
    <linearGradient id="ribbon-top" x1="120" y1="0" x2="650" y2="0" gradientUnits="userSpaceOnUse">
      <stop offset="0" stop-color="var(--pink)"/>
      <stop offset="0.5" stop-color="#d8405e"/>
      <stop offset="1" stop-color="#a8344f"/>
    </linearGradient>
    <linearGradient id="ribbon-bottom" x1="118" y1="0" x2="650" y2="0" gradientUnits="userSpaceOnUse">
      <stop offset="0" stop-color="#1aa59a"/>
      <stop offset="0.28" stop-color="#5fb68a"/>
      <stop offset="0.52" stop-color="#f0a33a"/>
      <stop offset="0.75" stop-color="#d24a3a"/>
      <stop offset="1" stop-color="#b01c3a"/>
    </linearGradient>
    <filter id="panel-shadow" x="-10%" y="-10%" width="120%" height="120%">
      <feDropShadow dx="0" dy="4" stdDeviation="6" flood-color="#000" flood-opacity="0.6"/>
    </filter>
  </defs>

  <!-- Chart stage -->
  <g class="chart-stage">
    <rect x="0" y="0" width="780" height="553" fill="url(#stage-bg)"/>
    <circle cx="145" cy="50" r="80" fill="none" stroke="#ffffff" stroke-opacity="0.04" stroke-width="18"/>
    <circle cx="40" cy="505" r="80" fill="none" stroke="#ffffff" stroke-opacity="0.05" stroke-width="18"/>
    <rect class="chart-panel" x="37" y="27" width="707" height="500" rx="12" fill="var(--panel)" filter="url(#panel-shadow)"/>
    <circle cx="670" cy="410" r="82" fill="none" stroke="#ffffff" stroke-opacity="0.05" stroke-width="18"/>

    <g class="price-bars">
      <rect x="181" y="290" width="159" height="172" fill="url(#bar-teal)"/>
      <rect x="340" y="262" width="147" height="200" fill="url(#bar-gold)"/>
      <rect x="487" y="200" width="126" height="262" fill="url(#bar-red)"/>
    </g>

    <g class="chart-axes" stroke="var(--white)" stroke-width="2" fill="var(--white)">
      <line x1="119" y1="462" x2="119" y2="104"/>
      <polygon points="119,96 114,107 124,107" stroke="none"/>
      <line x1="119" y1="462" x2="670" y2="462"/>
      <polygon points="680,462 669,457 669,467" stroke="none"/>
    </g>
    <text class="axis-label" x="117" y="86">Price</text>
    <text class="axis-label" x="655" y="499">Time</text>
    <text class="trend-label" x="621" y="122">Price Trend</text>

    <polygon class="trend-ribbon" fill="url(#ribbon-top)"
      points="120,283 260,300 410,266 549,216 616,172 606,158 650,143 634,188 624,180 553,238 414,284 260,311 120,284"/>

    <text class="tagline" x="260" y="206">Signup Today</text>
    <text class="tagline tagline--bold" x="260" y="230">for Huge Savings!</text>

    <g class="price-point price-point--today">
      <circle cx="260" cy="307" r="52" fill="url(#teal-fill)" stroke="var(--white)" stroke-width="4"/>
      <text class="price" x="260" y="316" font-size="26">$ 6,500</text>
      <text class="point-title" x="256" y="385" font-size="19">Today</text>
      <text class="point-sub" x="256" y="407" font-size="18">Price</text>
    </g>
    <g class="price-point price-point--30">
      <circle cx="412" cy="275" r="41" fill="url(#gold-fill)" stroke="#bdbdbd" stroke-width="4"/>
      <text class="price price--faded" x="412" y="283" font-size="21">$ 7,280</text>
      <text class="point-title" x="412" y="347" font-size="16" fill="#d6d6d6">30 Days</text>
      <text class="point-sub point-sub--muted" x="412" y="367" font-size="16">Price</text>
    </g>
    <g class="price-point price-point--90">
      <circle cx="549" cy="228" r="36" fill="url(#red-fill)" stroke="#bdbdbd" stroke-width="4"/>
      <text class="price price--faded" x="549" y="235" font-size="17">$ 7,460</text>
      <text class="point-title" x="549" y="292" font-size="14" fill="#cfcfcf">90 Days</text>
      <text class="point-sub point-sub--muted" x="549" y="310" font-size="14">Price</text>
    </g>
  </g>

  <!-- Timeline stage -->
  <g class="timeline-stage">
    <rect x="0" y="553" width="780" height="553" fill="var(--ink-dark)"/>

    <polygon class="trend-ribbon" fill="url(#ribbon-bottom)"
      points="118,775 259,801 396,768 521,725 612,672 602,659 650,638 628,684 620,678 526,742 400,783 259,810 118,776"/>
    <text class="trend-label trend-label--bold" x="506" y="691">Price Trend</text>

    <g class="connectors" stroke-width="1.5">
      <line x1="259" y1="805" x2="259" y2="838" stroke="var(--teal-a)"/>
      <line x1="396" y1="775" x2="396" y2="848" stroke="#e3a53a"/>
      <line x1="521" y1="733" x2="521" y2="853" stroke="#c0283a"/>
    </g>

    <g class="price-card price-card--today">
      <rect x="181" y="838" width="158" height="133" rx="6" fill="url(#teal-fill)"/>
      <text class="point-title" x="257" y="882" font-size="19">Today</text>
      <text class="point-sub" x="257" y="904" font-size="18">Price</text>
      <text class="price" x="260" y="944" font-size="26">$ 6,500</text>
    </g>
    <g class="price-card price-card--30">
      <rect x="340" y="848" width="125" height="115" rx="5" fill="url(#gold-fill)"/>
      <text class="point-title" x="397" y="882" font-size="16">30 Days</text>
      <text class="point-sub" x="397" y="902" font-size="16">Price</text>
      <text class="price" x="397" y="938" font-size="21">$ 7,280</text>
    </g>
    <g class="price-card price-card--90">
      <rect x="467" y="853" width="115" height="103" rx="5" fill="url(#red-fill)"/>
      <text class="point-title" x="525" y="886" font-size="15">90 Days</text>
      <text class="point-sub" x="525" y="904" font-size="14">Price</text>
      <text class="price" x="525" y="934" font-size="18">$ 7,460</text>
    </g>

    <g class="node-dots" fill="var(--white)" stroke-width="2">
      <circle cx="259" cy="805" r="5" stroke="var(--teal-a)"/>
      <circle cx="259" cy="838" r="5" stroke="var(--teal-a)"/>
      <circle cx="396" cy="775" r="5" stroke="#f0a33a"/>
      <circle cx="396" cy="848" r="5" stroke="#f0a33a"/>
      <circle cx="521" cy="733" r="5" stroke="#c0283a"/>
      <circle cx="521" cy="853" r="5" stroke="#c0283a"/>
    </g>

    <text class="tagline" x="260" y="1007">Signup Today</text>
    <text class="tagline tagline--bold" x="260" y="1031">for Huge Savings!</text>
  </g>
</svg>
</body>
</html>
```